Design a (20.4 x 10.14) Banner that says - Keep Hope Rising From Harvest Crown TV Family

We want a design (20.4 x 10.14) with the words 'Keep Hope Rising' as the main text and 'From Harvest Crown TV Family' underneath. For 'Harvest Crown TV', we'd like you to use the logo which can be found in the image attached.

The image attached is just an example but please let your creative juices flow!

Target Market(s)

Christian

Industry/Entity Type

Christian

Requirements
Must have
• Must have the words 'Keep Hope Rising' and 'From Harvest Crown TV Family'.

```html
<!DOCTYPE html>
<html lang="en">
<head>
<meta charset="utf-8">
<title>Keep Hope Rising – Harvest Crown TV Family</title>
<link rel="stylesheet" href="https://fonts.googleapis.com/css2?family=Arimo:wght@400;700&family=Pinyon+Script&display=swap">
<style>
  :root {
    --sky-glow: #ffd45a;
    --sky-orange: #f29a1c;
    --sky-deep: #c0520c;
    --sky-dark: #3e1604;
    --band-yellow: #f4e33a;
    --band-pale: #f8ee7a;
    --title-white: #ffffff;
    --title-brown: #5a1608;
    --tag-brown: #3a1406;
    --brand-navy: #1b2f86;
  }
  html, body {
    margin: 0;
    padding: 0;
    overflow: hidden;
    background: #ffffff;
  }
  .banner {
    position: relative;
    width: 1200px;
    height: 597px;
    overflow: hidden;
    font-family: "Arimo", Arial, sans-serif;
  }
  .banner__scene {
    position: absolute;
    inset: 0;
    background:
      radial-gradient(ellipse 45% 38% at 74% 44%, var(--sky-glow) 0%, rgba(255,200,60,0.6) 35%, rgba(242,154,28,0) 75%),
      radial-gradient(ellipse 85% 75% at 60% 45%, var(--sky-orange) 0%, var(--sky-deep) 55%, var(--sky-dark) 100%),
      var(--sky-deep);
  }
  .banner__scene::after {
    content: "";
    position: absolute;
    left: 0; right: 0; bottom: 0;
    height: 45%;
    background: linear-gradient(to bottom, rgba(62,22,4,0) 0%, rgba(62,22,4,0.55) 100%);
  }
  .banner__bands {
    position: absolute;
    inset: 0;
    width: 1200px;
    height: 597px;
  }
  .headline {
    position: absolute;
    left: 420px;
    top: 108px;
    margin: 0;
    font-weight: 400;
    line-height: 1;
  }
  .headline__script {
    display: block;
    font-family: "Pinyon Script", cursive;
    font-size: 96px;
    color: var(--title-brown);
    line-height: 0.8;
  }
  .headline__main {
    display: block;
    margin-top: -6px;
    font-family: "Arimo", Arial, sans-serif;
    font-size: 116px;
    letter-spacing: -5px;
    line-height: 1;
    white-space: nowrap;
  }
  .headline__light { color: var(--title-white); }
  .headline__dark { color: var(--title-brown); }
  .tagline {
    position: absolute;
    left: 576px;
    top: 284px;
    margin: 0;
    font-size: 26px;
    color: var(--tag-brown);
  }
  .brand {
    position: absolute;
    left: 32px;
    bottom: 22px;
    display: flex;
    align-items: center;
    gap: 10px;
    font-size: 28px;
    font-weight: 700;
    color: var(--brand-navy);
  }
  .brand__dot {
    width: 22px;
    height: 22px;
    border-radius: 50%;
    background: var(--brand-navy);
  }
</style>
</head>
<body>
<main class="banner">
  <div class="banner__scene" role="img" aria-label="Photograph of a couple in silhouette walking hand in hand above the clouds at a golden sunset"></div>

  <svg class="banner__bands" viewBox="0 0 1200 597" aria-hidden="true">
    <path d="M0 0 L420 0 Q200 60 0 230 Z" fill="var(--band-pale)" opacity="0.45"/>
    <path d="M600 0 L1200 0 L1200 22 Q900 8 600 0 Z" fill="var(--band-yellow)" opacity="0.8"/>
    <path d="M0 597 L0 300 Q120 440 330 597 Z" fill="var(--band-pale)" opacity="0.35"/>
    <path d="M0 597 L0 500 Q320 470 640 420 Q960 370 1200 300 L1200 597 Z" fill="var(--band-yellow)" opacity="0.45"/>
    <path d="M0 597 L0 520 Q200 500 420 530 Q760 560 1200 440 L1200 597 Z" fill="var(--band-yellow)" opacity="0.85"/>
    <path d="M0 597 L0 560 Q600 580 1200 520 L1200 597 Z" fill="var(--band-pale)"/>
  </svg>

  <h1 class="headline">
    <span class="headline__script">Keep</span>
    <span class="headline__main"><span class="headline__light">HOPE</span><span class="headline__dark">RISING</span></span>
  </h1>
  <p class="tagline">from Harvest Crown TV Family</p>

  <div class="brand">
    <span class="brand__name">Harvest Crown TV</span>
    <span class="brand__dot"></span>
  </div>
</main>
</body>
</html>
```